web design needed for jewellery inspired temporary tattoo company

Hi There

I need a web design for a new company I'm launching called coral glow luxe
Im a retailer of flash tattoos - temporary gold and silver metallic tattoos

These are the next new craze with many celebrities already displaying them whilst being lapped on their holidays

i need a very classy upmarket wow web design with an e commerce shop attached

I also offer marlow q bronze mist so will need a page to link to where people can get a tan and tattoo - so maybe as a box on the main page

As A guide I'm looking for someone to put their unique spin on an american website which is currently selling the same type of product
www.glintmarkz.com

the final design should oozzzz 'rich list ' coral luxe - think st tropez Monaco and needs to be linked to all my social media

please seepintrest flash tattoos for what we sell
I've attached my logo

I can't wait to hear from you all
many Thanks

Fiona Dembrey
www.coralglowluxe.co.uk

Target Market(s)

20 to 30's young party rich list glamous girls - festival boho cool beach LA

Industry/Entity Type

It Company

Number of Pages Required

3 page

Font styles to use
Script

Requirements
Must have
• a beach feel
• pictures of people wearing the tattoos
• an ecommerce site
• be easy to navigate
• my logo
• the wow factor
Nice to have
• a really classy expensive feel to the website
Should not have
• a cheap plain look

```html
<!DOCTYPE html>
<html lang="en">
<head>
<meta charset="utf-8">
<title>Coral Glow Luxe</title>
<link rel="stylesheet" href="https://fonts.googleapis.com/css2?family=Marcellus&family=Montserrat:wght@400;500;600&family=Raleway:wght@400;500;600&display=swap">
<style>
:root{
  --black:#000;
  --dark:#1b1b1b;
  --footer:#1a1a1a;
  --gold:#e3aa2b;
  --gold-light:#f2c24e;
  --gold-deep:#c98f1a;
  --sun-top:#f6c95e;
  --sun-bottom:#eda231;
  --ink:#1e1e1e;
  --text:#444;
  --muted:#8a8a8a;
  --line:#dcdcdc;
  --white:#fff;
}
*{margin:0;padding:0;box-sizing:border-box}
html,body{width:1200px;height:2305px;overflow:hidden}
body{position:relative;background:var(--white);font-family:"Raleway",Arial,sans-serif;color:var(--text)}
a{color:inherit;text-decoration:none}

.site-header{position:absolute;left:0;top:0;width:1200px;height:356px;background:var(--black)}
.brand{position:absolute;left:0;top:18px;width:1200px;text-align:center;color:var(--gold)}
.brand-mark{display:block;margin:0 auto 12px;width:86px;height:86px;border-radius:50%;background:var(--gold)}
.brand-name{font-family:"Marcellus",Georgia,serif;font-size:28px;color:var(--gold);line-height:1}
.brand-city{font-family:"Marcellus",Georgia,serif;font-size:12px;letter-spacing:2px;color:var(--gold);margin-top:8px}

.account-links{position:absolute;left:731px;top:20px;display:flex;align-items:center;font-family:"Montserrat",Arial,sans-serif;font-size:10px;color:#ddd}
.account-links a{color:#ddd}
.account-links .sep{margin:0 8px;color:#999}
.cart-icon{margin-left:10px;width:18px;height:16px}

.main-nav{position:absolute;left:187px;top:178px;width:827px;height:48px;display:flex;background:linear-gradient(to bottom,var(--gold-light),var(--gold) 55%,var(--gold-deep))}
.main-nav a{display:flex;align-items:center;justify-content:center;font-family:"Montserrat",Arial,sans-serif;font-weight:600;font-size:12.5px;color:var(--white);border-right:1px solid rgba(255,255,255,.35)}
.main-nav a:last-child{border-right:0}

.hero{position:absolute;left:187px;top:226px;width:827px;height:370px}
.hero-photo{position:absolute;inset:0;background:linear-gradient(90deg,#3c4a32 0%,#8d6a4c 25%,#c99470 45%,#4b463f 50%,#8a8276 70%,#b89b84 100%)}
.hero-caption{position:absolute;left:171px;top:110px;width:482px;height:120px;background:rgba(20,20,20,.6);text-align:center;color:var(--white);font-family:"Montserrat",Arial,sans-serif}
.hero-caption h1{font-weight:500;font-size:39px;letter-spacing:1px;margin-top:20px;line-height:1.1}
.hero-caption p{font-size:24px;letter-spacing:4.5px;line-height:1.1;margin-top:2px}
.hero-dots{position:absolute;left:378px;top:343px;display:flex;gap:6px}
.hero-dots span{width:14px;height:14px;border-radius:50%;background:var(--white)}

.intro{position:absolute;left:0;top:638px;width:1200px;text-align:center;color:var(--ink)}
.intro h2{font-family:"Montserrat",Arial,sans-serif;font-weight:500;font-size:26px;letter-spacing:.5px}
.intro h3{font-family:"Montserrat",Arial,sans-serif;font-weight:500;font-size:18px;margin-top:8px}
.intro p{width:830px;margin:18px auto 0;font-size:9.2px;line-height:16px;color:#333}
.intro p + p{margin-top:10px;white-space:nowrap}

.feature{position:absolute;left:0;width:1200px;display:flex}
.feature-one{top:836px;height:381px}
.feature-two{top:1217px;height:385px}
.feature-text{width:600px;padding-left:187px;display:flex;flex-direction:column;justify-content:center}
.feature-two .feature-text{padding-left:50px}
.feature-photo{width:600px;height:100%}
.feature-one .feature-text{background:var(--dark);color:var(--white)}
.feature-two .feature-text{background:linear-gradient(to bottom,var(--sun-top),var(--sun-bottom));color:var(--ink)}
.feature h2{font-family:"Marcellus",Georgia,serif;font-weight:400;font-size:29px;letter-spacing:.5px}
.feature h3{font-family:"Marcellus",Georgia,serif;font-weight:400;font-size:24px;margin-top:4px}
.feature p{width:340px;font-size:9px;line-height:16px;margin-top:12px}
.feature-one p{color:#5e5e5e}
.feature-two p{color:#6b5320}
.btn{display:inline-flex;align-items:center;justify-content:center;width:94px;height:27px;margin-top:16px;font-family:"Montserrat",Arial,sans-serif;font-size:10px;font-weight:600;border-radius:3px}
.btn-gold{background:linear-gradient(to bottom,var(--gold-light),var(--gold));color:#2a1e05}
.btn-dark{background:#141414;color:var(--white)}
.photo-ankle{background:linear-gradient(135deg,#5a5147 0%,#8c7f71 40%,#6b5f52 70%,#a69886 100%)}
.photo-back{background:linear-gradient(to bottom,#c9c2b4 0%,#8a7a6c 40%,#6b4a38 60%,#8a7560 100%)}

.featured{position:absolute;left:0;top:1652px;width:1200px}
.featured h2{text-align:center;font-family:"Marcellus",Georgia,serif;font-weight:400;font-size:24px;color:var(--ink)}
.product-grid{position:absolute;left:186px;top:53px;width:823px;height:261px;display:flex;border:1px solid var(--line);box-shadow:0 14px 18px -10px rgba(0,0,0,.18)}
.product{width:25%;border-right:1px solid var(--line);display:flex;flex-direction:column}
.product:last-child{border-right:0}
.product-photo{height:144px}
.product h4{text-align:center;font-weight:500;font-size:15px;color:var(--ink);margin-top:14px}
.product p{text-align:center;font-size:8.5px;line-height:13px;color:var(--muted);margin-top:6px}
.product-buy{margin-top:auto;height:36px;border-top:1px solid var(--line);display:flex}
.price{width:50%;display:flex;align-items:center;padding-left:20px;color:var(--gold);font-size:17px}
.price small{font-size:11px;margin-right:4px}
.add-cart{width:50%;display:flex;align-items:center;justify-content:center;border-left:1px solid var(--line);font-size:11px;color:var(--ink)}
.p1{background:linear-gradient(135deg,#2c211c,#7a5a45 60%,#b08a6c)}
.p2{background:linear-gradient(135deg,#6a7d7a,#a88a62 50%,#c9a77a)}
.p3{background:linear-gradient(to bottom,#3c8c93,#9b7258 50%,#6b4635)}
.p4{background:linear-gradient(to bottom,#a8c6d6,#c9b7a3 55%,#a47e62)}

.site-footer{position:absolute;left:0;top:2035px;width:1200px;height:270px;background:var(--footer);color:var(--white)}
.footer-col{position:absolute;top:48px}
.footer-col h5{font-family:"Marcellus",Georgia,serif;font-weight:400;font-size:16px;letter-spacing:.3px}
.footer-col ul{list-style:none;margin-top:9px}
.footer-col li{font-size:10.5px;color:#a4a4a4;line-height:22px}
.newsletter p{font-size:10.5px;color:#a4a4a4;margin-top:9px}
.newsletter-field{margin-top:8px;width:189px;height:25px;background:#333;display:flex;align-items:center;justify-content:space-between;padding:0 9px;font-size:9px;color:#8a8a8a}
.social-links{list-style:none;display:grid;grid-template-columns:auto auto;column-gap:14px;row-gap:6px;margin-top:12px}
.social-links a{display:flex;align-items:center;gap:6px;font-size:11px;font-weight:600;color:var(--white)}
.social-links a::before{content:"";width:8px;height:8px;border-radius:50%;background:var(--gold)}
.footer-rule{position:absolute;left:187px;top:215px;width:827px;height:1px;background:#2c2c2c}
.copyright{position:absolute;left:187px;top:231px;font-size:9px;color:#7a7a7a}
</style>
</head>
<body>

<header class="site-header">
  <div class="brand">
    <span class="brand-mark"></span>
    <div class="brand-name">Coral Glow Luxe</div>
    <div class="brand-city">LONDON</div>
  </div>
  <nav class="account-links">
    <a href="#">MY ACCOUNT</a><span class="sep">|</span>
    <a href="#">LOGIN</a><span class="sep">|</span>
    <a href="#">SIGN UP</a><span class="sep">|</span>
    <a href="#">MY CART</a>
    <svg class="cart-icon" viewBox="0 0 18 16" aria-hidden="true"><path d="M0 1h3l3 9h9l2-7H5" fill="none" stroke="#e3aa2b" stroke-width="2"/><path d="M5 3h12l-2 7H6z" fill="#e3aa2b"/><circle cx="7" cy="14" r="1.6" fill="#e3aa2b"/><circle cx="14" cy="14" r="1.6" fill="#e3aa2b"/></svg>
  </nav>
</header>

<nav class="main-nav">
  <a href="#" style="width:103px">HOME</a>
  <a href="#" style="width:105px">ABOU US</a>
  <a href="#" style="width:204px">QUESTIONS &amp; ANSWERS</a>
  <a href="#" style="width:181px">SPRAY TAN SERVICES</a>
  <a href="#" style="width:109px">BUY NOW</a>
  <a href="#" style="width:125px">CONTACT</a>
</nav>

<section class="hero">
  <div class="hero-photo" role="img" aria-label="Arms and feet decorated with gold metallic temporary tattoos on grass and sand"></div>
  <div class="hero-caption">
    <h1>THEYRE NON TOXIC</h1>
    <p>DONEC DICTUM LECTUS</p>
  </div>
  <div class="hero-dots"><span></span><span></span><span></span><span></span></div>
</section>

<section class="intro">
  <h2>MAURIS VEL LACUS VITAE FELIS VESTIBULUM</h2>
  <h3>CUM SOCIIS NATOQUE PENATIBUS ET MAGNIS DIS</h3>
  <p>Curabitur iaculis tempus eros Curabitur vel mi sit amet magna malesuada ultrices Ut nisi erat fermentum vel congue id euismod in elit Fusce ultricies orci ac feugiat suscipit leo massa sodales velit et scelerisque mi tortor at ipsum cligula augue bibendum accumsan vestibulum ut commodo a mi Morbi ornare gravida elit Integer congue augue et malesuada iaculis ipsum dui aliquet felis at cursus magna nisl nec elit Praesent elementum elit at tellus nec ultricies sit amet porttitor mattis enim In massa libero interdum nec interdum vel</p>
  <p>Cras a ante vitae enim iaculis aliquam Mauris nunc quam venenatis nec euismod sit amet egestas placerat est Pellentesque habitant morbi tristique senectus et netus et malesuada</p>
</section>

<section class="feature feature-one">
  <div class="feature-text">
    <h2>CUM SOCIIS NATOQUE</h2>
    <h3>Pellentesque faucibus accumsa</h3>
    <p>Aalesuada ultrices Ut nisi erat fermentum vel congue id euismod in elit Fusce ultricies orci ac feugiat suscipit leo massa sodales velit et scelerisque mi tortor at ipsum cligula augue bibendum accumsan vestibulum</p>
    <a href="#" class="btn btn-gold">CLICK HERE</a>
  </div>
  <div class="feature-photo photo-ankle" role="img" aria-label="Feet on sand wearing silver and gold metallic tattoo anklets"></div>
</section>

<section class="feature feature-two">
  <div class="feature-photo photo-back" role="img" aria-label="Woman on the beach seen from behind with a gold tattoo down her spine"></div>
  <div class="feature-text">
    <h2>AENEAN PORTTITOR EROS</h2>
    <h3>Mauris nunc quam venenatis</h3>
    <p>Aalesuada ultrices Ut nisi erat fermentum vel congue id euismod in elit Fusce ultricies orci ac feugiat suscipit leo massa sodales velit et scelerisque mi tortor at ipsum cligula augue bibendum accumsan vestibulum</p>
    <a href="#" class="btn btn-dark">CLICK HERE</a>
  </div>
</section>

<section class="featured">
  <h2>FEATURED &amp; MOST POPULAR</h2>
  <div class="product-grid">
    <article class="product">
      <div class="product-photo p1" role="img" aria-label="Back wearing a gold spine tattoo"></div>
      <h4>Mauris nunc quam</h4>
      <p>Phasellus pellentesque aliquam enim<br>Proin dui lectus cursus eu mattis</p>
      <div class="product-buy"><span class="price"><small>$</small>25.99</span><a href="#" class="add-cart">ADD TO CART</a></div>
    </article>
    <article class="product">
      <div class="product-photo p2" role="img" aria-label="Wrists stacked with gold metallic tattoo bracelets"></div>
      <h4>Cras a ante vitae enim</h4>
      <p>Phasellus pellentesque aliquam enim<br>Proin dui lectus cursus eu mattis</p>
      <div class="product-buy"><span class="price"><small>$</small>25.99</span><a href="#" class="add-cart">ADD TO CART</a></div>
    </article>
    <article class="product">
      <div class="product-photo p3" role="img" aria-label="Tanned back with gold tattoo by the sea"></div>
      <h4>Praesent vitae lacus</h4>
      <p>Phasellus pellentesque aliquam enim<br>Proin dui lectus cursus eu mattis</p>
      <div class="product-buy"><span class="price"><small>$</small>25.99</span><a href="#" class="add-cart">ADD TO CART</a></div>
    </article>
    <article class="product">
      <div class="product-photo p4" role="img" aria-label="Woman at the beach with gold tattoos on her back"></div>
      <h4>Integer quis urna</h4>
      <p>Phasellus pellentesque aliquam enim<br>Proin dui lectus cursus eu mattis</p>
      <div class="product-buy"><span class="price"><small>$</small>25.99</span><a href="#" class="add-cart">ADD TO CART</a></div>
    </article>
  </div>
</section>

<footer class="site-footer">
  <div class="footer-col" style="left:197px">
    <h5>COMPANY</h5>
    <ul><li>Home</li><li>About Us</li><li>Tattos</li><li>Most Popular</li></ul>
  </div>
  <div class="footer-col" style="left:339px">
    <h5>RESOURCES</h5>
    <ul><li>Caring &amp; Sharing</li><li>Privacy Statement</li><li>Contact Us</li><li>Distributors</li></ul>
  </div>
  <div class="footer-col" style="left:491px">
    <h5>SUPPORT</h5>
    <ul><li>My Account</li><li>Free Shipping</li><li>Support</li><li>Term of Use</li></ul>
  </div>
  <div class="footer-col newsletter" style="left:617px">
    <h5>NEWSELTTER SIGN UP</h5>
    <p>Please sign up here for latest offers.</p>
    <div class="newsletter-field">
      <span>Email address</span>
      <svg width="7" height="10" viewBox="0 0 7 10" aria-hidden="true"><path d="M1 1l4 4-4 4" fill="none" stroke="#fff" stroke-width="1.5"/></svg>
    </div>
  </div>
  <div class="footer-col" style="left:851px">
    <h5>STAY IN TOUCH</h5>
    <ul class="social-links">
      <li><a href="#">Chirpline</a></li>
      <li><a href="#">Friendwall</a></li>
      <li><a href="#">Workring</a></li>
      <li><a href="#">Circlepost</a></li>
    </ul>
  </div>
  <div class="footer-rule"></div>
  <p class="copyright">© 2015 Company Name. All right reserved. Term of Use</p>
</footer>

</body>
</html>
```